Beacon Advisory Website

I currently have a website www.beaconadvisoryinc.example. We are a IT Consulting Company. Our website will pretty much tell out our services. I am looking to enhance my website and make it look more professional. Looking for very classy and Contemporary look and design for my website.

Industry/Entity Type

It Company

```html
<!DOCTYPE html>
<html lang="en">
<head>
<meta charset="utf-8">
<title>Beacon Advisory</title>
<link rel="stylesheet" href="https://fonts.googleapis.com/css2?family=Open+Sans:wght@400;600&display=swap">
<style>
:root{
  --blue:#1a5ba8;
  --navy:#0d3c85;
  --ink:#2b2b2b;
  --muted:#8a8a8a;
  --band:#f1f1f1;
  --footer:#3b3b3b;
  --footer-text:#bdbdbd;
  --white:#ffffff;
}
*{margin:0;padding:0;box-sizing:border-box}
html,body{width:891px;height:1200px;overflow:hidden}
body{font-family:"Open Sans",Arial,sans-serif;background:var(--white);color:var(--ink);position:relative}
.abs{position:absolute}

/* header */
.site-header{position:absolute;left:0;top:0;width:891px;height:66px;background:var(--white)}
.brand{left:98px;top:18px;display:flex;align-items:center;gap:8px}
.brand-mark{width:26px;height:26px;border-radius:50%;background:var(--blue)}
.brand-name{font-size:17px;font-weight:600;color:var(--navy);letter-spacing:.2px}
.main-nav{right:99px;top:24px;display:flex;gap:21px;font-size:8.5px;color:#444}
.main-nav .active{color:var(--blue);display:flex;align-items:center;gap:5px}
.main-nav .active::before{content:"";width:9px;height:9px;border-radius:2px;background:var(--blue)}

/* hero */
.hero{left:0;top:66px;width:891px;height:262px;background:linear-gradient(100deg,#8e99a3 0%,#c7cdd2 35%,#e8e6e1 60%,#d8c8b0 100%)}
.hero-caption{right:99px;top:42px;text-align:right;font-size:14.5px;line-height:19px;color:#111}
.hero-dots{left:416px;top:232px;width:58px;height:12px;border-radius:6px;background:rgba(40,40,40,.55);display:flex;align-items:center;justify-content:center;gap:7px}
.hero-dots span{width:5px;height:5px;border-radius:50%;background:#fff}
.hero-dots span:first-child{background:transparent;border:1px solid #fff}

/* welcome */
.welcome{left:0;top:328px;width:891px;height:128px;background:var(--band);text-align:center}
.welcome h1{position:absolute;left:0;width:891px;top:12px;font-size:16px;font-weight:400;color:var(--blue)}
.welcome p{position:absolute;left:98px;width:694px;top:38px;font-size:7.3px;line-height:14.4px;color:#777}
.btn-outline{left:416px;top:89px;width:59px;height:24px;border:1px solid #ddd;background:#fff;font-size:7.5px;color:#888;display:flex;align-items:center;justify-content:center}

/* services */
.service{width:210px}
.service svg{display:block;width:20px;height:20px}
.service h2{margin-top:14px;font-size:16px;font-weight:400;color:var(--blue);line-height:18px}
.service p{margin-top:6px;font-size:7.3px;line-height:13px;color:var(--muted)}
.service a{display:inline-block;margin-top:6px;font-size:7px;color:#222;text-decoration:underline}

/* cards */
.card{top:806px;width:223px;height:179px;overflow:hidden}
.card-photo{width:223px;height:147px}
.card-label{width:223px;height:32px;background:linear-gradient(#2a6cc0,#0c3b82);color:#fff;font-size:12.5px;padding-left:12px;display:flex;align-items:center}

/* cta */
.cta{left:0;top:1022px;width:891px;height:110px;background:var(--band);text-align:center}
.cta p{position:absolute;left:0;width:891px;top:22px;font-size:13px;color:#333}
.btn-solid{left:405px;top:51px;width:82px;height:35px;background:linear-gradient(#1c57a8,#0d3c85);color:#fff;font-size:11px;display:flex;align-items:center;justify-content:center}

/* footer */
.site-footer{left:0;top:1132px;width:891px;height:68px;background:var(--footer)}
.footer-nav{left:99px;top:18px;font-size:7.5px;color:var(--footer-text);display:flex;gap:7px}
.footer-nav .sep{color:#777}
.copyright{left:99px;top:38px;font-size:7.5px;color:var(--footer-text)}
.social{top:25px;width:19px;height:19px;border-radius:50%}
</style>
</head>
<body>

<header class="site-header">
  <div class="abs brand"><span class="brand-mark"></span><span class="brand-name">Beacon Advisory</span></div>
  <nav class="abs main-nav">
    <span class="active">Company</span><span>Services</span><span>Solutions</span><span>Resources</span><span>Career</span><span>Contact us</span>
  </nav>
</header>

<section class="abs hero" role="img" aria-label="Photo of a business team meeting around a conference table with laptops">
  <p class="abs hero-caption">Qualified IT and Management Professionals<br>from around the world</p>
  <div class="abs hero-dots"><span></span><span></span><span></span><span></span></div>
</section>

<section class="abs welcome">
  <h1>Welcome to Beacon Advisory</h1>
  <p>Today's IT market is a dynamic, fast-paced industry, with ever-increasing demands. Meeting these demands for over 25 years, Beacon Advisory maintains a global presence, aggressively recruiting expertly qualified IT and Management Professionals from around the world and cultivating key partnerships with corporations to understand their business models end-to-end, with a goal of delivering exceptional client service and ensuring a consistent delivery of the talent needed to drive results.</p>
  <span class="abs btn-outline">Read more</span>
</section>

<article class="abs service" style="left:98px;top:494px">
  <svg viewBox="0 0 20 20" fill="none" stroke="#0d3c85" stroke-width="1.8"><path d="M10 2a5 5 0 0 0-3 9v3h6v-3a5 5 0 0 0-3-9z"/><path d="M8 17h4"/></svg>
  <h2>Technology</h2>
  <p>Integer feugiat, dolor dignissim faucibus, neque elit biben dum erat, et molestie sapien tellus in ligula. Proin pellen tesque iaculis diam eget blandit.</p>
  <a>READ MORE</a>
</article>
<article class="abs service" style="left:342px;top:494px">
  <svg viewBox="0 0 20 20"><rect x="1" y="5" width="18" height="13" rx="1.5" fill="#0d3c85"/><path d="M7 5V3h6v2" fill="none" stroke="#0d3c85" stroke-width="1.8"/><rect x="1" y="10" width="18" height="1.2" fill="#fff"/></svg>
  <h2>Business</h2>
  <p>Integer feugiat, dolor dignissim faucibus, neque elit biben dum erat, et molestie sapien tellus in ligula. Proin pellen tesque iaculis diam eget blandit.</p>
  <a>READ MORE</a>
</article>
<article class="abs service" style="left:585px;top:494px">
  <svg viewBox="0 0 26 20" style="width:26px"><rect x="1" y="4" width="24" height="13" rx="1" fill="none" stroke="#0d3c85" stroke-width="1.6"/><path d="M4 8h18M4 11h18M7 14h12" stroke="#0d3c85" stroke-width="1.6" stroke-dasharray="1.5 1"/></svg>
  <h2>Application</h2>
  <p>Integer feugiat, dolor dignissim faucibus, neque elit biben dum erat, et molestie sapien tellus in ligula. Proin pellen tesque iaculis diam eget blandit.</p>
  <a>READ MORE</a>
</article>

<article class="abs service" style="left:98px;top:655px">
  <svg viewBox="0 0 20 20"><path d="M3 17l8-8" stroke="#0d3c85" stroke-width="3" stroke-linecap="round"/><circle cx="14" cy="6" r="4.5" fill="#0d3c85"/><circle cx="15.5" cy="4.5" r="2" fill="#fff"/></svg>
  <h2>Development</h2>
  <p>Integer feugiat, dolor dignissim faucibus, neque elit biben dum erat, et molestie sapien tellus in ligula. Proin pellen tesque iaculis diam eget blandit.</p>
  <a>READ MORE</a>
</article>
<article class="abs service" style="left:342px;top:655px">
  <svg viewBox="0 0 26 22" style="width:26px"><circle cx="9" cy="13" r="6" fill="none" stroke="#0d3c85" stroke-width="3.5" stroke-dasharray="2.2 1.4"/><circle cx="9" cy="13" r="2" fill="#0d3c85"/><circle cx="20" cy="6" r="3.5" fill="none" stroke="#0d3c85" stroke-width="2.5" stroke-dasharray="1.6 1"/><circle cx="20" cy="17" r="3" fill="none" stroke="#0d3c85" stroke-width="2.3" stroke-dasharray="1.5 1"/></svg>
  <h2>Enterprise Integration</h2>
  <p>Integer feugiat, dolor dignissim faucibus, neque elit biben dum erat, et molestie sapien tellus in ligula. Proin pellen tesque iaculis diam eget blandit.</p>
  <a>READ MORE</a>
</article>
<article class="abs service" style="left:585px;top:655px">
  <svg viewBox="0 0 26 20" style="width:26px"><ellipse cx="13" cy="9" rx="11.5" ry="7.5" fill="#0d3c85"/><path d="M5 14l-3 5 7-3z" fill="#0d3c85"/></svg>
  <h2>IT Consulting</h2>
  <p>Integer feugiat, dolor dignissim faucibus, neque elit biben dum erat, et molestie sapien tellus in ligula. Proin pellen tesque iaculis diam eget blandit.</p>
  <a>READ MORE</a>
</article>

<div class="abs card" style="left:98px">
  <div class="card-photo" role="img" aria-label="Photo of business people shaking hands" style="background:linear-gradient(135deg,#e6ecf2,#b9c6d3)"></div>
  <div class="card-label">Consulting</div>
</div>
<div class="abs card" style="left:334px">
  <div class="card-photo" role="img" aria-label="Photo of two colleagues planning at a wall of sticky notes" style="background:linear-gradient(135deg,#d8c48e,#e9dcc0 50%,#a9c2d6)"></div>
  <div class="card-label">Staff Augmentation</div>
</div>
<div class="abs card" style="left:569px">
  <div class="card-photo" role="img" aria-label="Photo of a business team in suits standing before a world map" style="background:linear-gradient(#4a5a70,#1c2430)"></div>
  <div class="card-label">Offshore</div>
</div>

<section class="abs cta">
  <p>Cum sociis natoque penatibus et magnis dis parturient montes</p>
  <span class="abs btn-solid">Apply Now</span>
</section>

<footer class="abs site-footer">
  <nav class="abs footer-nav">
    <span>Company</span><span class="sep">|</span><span>Services</span><span class="sep">|</span><span>Solutions</span><span class="sep">|</span><span>Resources</span><span class="sep">|</span><span>Career</span><span class="sep">|</span><span>Contact us</span>
  </nav>
  <p class="abs copyright">Copyright © 2016 Beacon Advisory. All rights reserved.</p>
  <span class="abs social" style="left:724px;background:#3c5a99"></span>
  <span class="abs social" style="left:748px;background:#2a9fd8"></span>
  <span class="abs social" style="left:773px;background:#1f6fb2"></span>
</footer>

</body>
</html>
```